Downtown hair salon need trendy website

I need a website with style. Unique. We need this site to list prices , Hair and nail services, service providers hours. I would also like my logo design on the website. We are located Downtown Grand rapids. Beautiful city with lots of culture.

Target Market(s)

Men and women

Industry/Entity Type

Hair And Beauty

Coding

Coded - Design and coding required

Number of Pages Required

3 page

Font styles to use
Sans Serif

Colors

Designer to choose colors to be used in the design.

Requirements
Must have
• Logo of business. Hours, services and prices, Page for pictures of each service provider. Nail service and prices. Products that we carry... Area on page for my mission statement.
Nice to have
• Pictures of trendy of the beauty industry. Men and women cuts.. Nails..
Should not have
• booking on line options...

```html
<!DOCTYPE html>
<html lang="en">
<head>
<meta charset="utf-8">
<title>Marlowe Downtown — Hair &amp; Beauty</title>
<link href="https://fonts.googleapis.com/css2?family=Roboto:wght@300;400;500;700&display=swap" rel="stylesheet">
<style>
:root{
  --gold:#b8862a;
  --black:#000;
  --ink:#111;
  --text:#444;
  --muted:#6d6d6d;
  --white:#fff;
  --hero-a:#2a1a12;
  --hero-b:#120b07;
}
*{margin:0;padding:0;box-sizing:border-box}
html,body{width:1200px;height:2694px;overflow:hidden;background:var(--white)}
body{position:relative;font-family:'Roboto',Arial,sans-serif;color:var(--text)}
.abs{position:absolute}

/* header */
.site-header{left:0;top:0;width:1200px;height:163px;background:var(--black)}
.brand{left:186px;top:40px;width:120px;text-align:center}
.brand-name{display:block;color:var(--gold);font-weight:500;font-size:24px;letter-spacing:1px;line-height:28px}
.brand-sub{display:block;color:var(--white);font-size:9px;letter-spacing:3px;margin-top:2px}
.nav{left:403px;top:47px;display:flex;gap:28px;font-size:11px;font-weight:500;color:var(--white)}
.nav a{color:inherit;text-decoration:none}
.nav .active{color:var(--gold);border-bottom:2px solid var(--gold);padding-bottom:5px}
.btn-outline-header{left:873px;top:39px;width:140px;height:35px;border:1px solid var(--white);color:var(--white);font-size:11px;display:flex;align-items:center;justify-content:center}

/* hero */
.hero{left:0;top:163px;width:1200px;height:454px;background:radial-gradient(ellipse at 55% 20%,#4a3324 0%,var(--hero-a) 40%,var(--hero-b) 100%)}
.hero-kicker{left:0;top:248px;width:1200px;text-align:center;color:var(--white);font-size:22px;font-weight:500;letter-spacing:1px}
.hero-kicker span{color:var(--gold)}
.hero-title{left:0;top:300px;width:1200px;text-align:center;color:var(--white);font-size:36px;font-weight:700;letter-spacing:2px;line-height:42px}
.btn{display:flex;align-items:center;justify-content:center;font-size:12px;color:var(--white)}
.btn-ghost{left:491px;top:440px;width:97px;height:38px;border:1px solid var(--white)}
.btn-gold{background:var(--gold)}
.hero-prices{left:612px;top:440px;width:97px;height:38px}

/* about */
.about-photo{left:64px;top:665px;width:497px;height:472px;background:linear-gradient(135deg,#f1f1f4 0%,#d9c2ad 45%,#8a4e2c 100%)}
.section-heading{color:var(--gold);font-weight:500;font-size:30px;letter-spacing:1px}
.rule{height:4px;width:84px;background:var(--gold)}
.about-heading{left:619px;top:727px}
.about-rule{left:619px;top:773px}
.about-sub{left:619px;top:797px;width:440px;color:var(--ink);font-size:26px;font-weight:500;line-height:32px;white-space:nowrap}
.about-copy{left:619px;top:886px;width:400px;font-size:15.5px;line-height:19px;color:var(--text)}
.about-copy p+p{margin-top:19px}
.about-btn{left:619px;top:1077px;width:96px;height:37px}

/* services */
.service-band{left:0;top:1227px;width:1200px;height:581px;background:linear-gradient(90deg,#2c1d16 0%,#140d0a 45%,#000 75%)}
.service-heading{left:0;top:1277px;width:1200px;text-align:center}
.service-rule{left:558px;top:1325px}
.service-card{left:187px;top:1424px;width:826px;height:708px;background:var(--white);box-shadow:0 4px 10px rgba(0,0,0,.35)}
.service{position:absolute;width:220px;text-align:center}
.service-thumb{width:140px;height:140px;margin:0 auto;border-radius:50%;border:4px solid var(--gold)}
.service h3{margin-top:18px;font-size:21px;font-weight:500;color:var(--ink)}
.service p{margin:10px auto 0;font-size:9.5px;line-height:11px;color:var(--muted);width:210px}
.service .more{display:block;margin-top:8px;font-size:11px;font-weight:500;color:var(--gold)}
.card-btn{left:530px;top:2040px;width:140px;height:33px}

/* footer */
.footer-brand{left:187px;top:2390px;width:140px;text-align:center}
.footer-brand .brand-name{font-size:28px;line-height:32px}
.footer-brand .brand-sub{color:var(--ink);font-size:10px}
.footer-about{left:187px;top:2453px;width:250px;font-size:12px;line-height:14px;color:var(--muted)}
.footer-col h4{font-size:16px;font-weight:500;color:var(--ink);margin-bottom:14px}
.footer-col ul{list-style:none;font-size:12.5px;color:var(--muted)}
.footer-col li{position:relative;padding-left:21px;line-height:15px;margin-bottom:14px}
.footer-col.links li::before,.footer-col.hours li::before{content:"";position:absolute;left:0;top:4px;border-left:5px solid var(--gold);border-top:3.5px solid transparent;border-bottom:3.5px solid transparent}
.links{left:494px;top:2340px}
.hours{left:622px;top:2340px;width:170px}
.hours li{margin-bottom:10px}
.touch{left:835px;top:2340px;width:200px}
.touch-line{position:absolute;left:26px;font-size:12.5px;line-height:15px;color:var(--muted);white-space:nowrap}
.touch svg{position:absolute;left:0}
.socials{left:472px;top:2546px;display:flex;gap:17px}
.socials span{width:38px;height:38px;border-radius:50%;background:var(--gold);display:block}
.copyright-bar{left:0;top:2618px;width:1200px;height:76px;background:var(--gold);display:flex;align-items:center;justify-content:center;font-size:12px;color:#f2dfb8}
</style>
</head>
<body>

<header class="abs site-header"></header>
<div class="abs brand"><span class="brand-name">MARLOWE</span><span class="brand-sub">DOWNTOWN</span></div>
<nav class="abs nav">
  <a class="active" href="#">Home</a><a href="#">Womens</a><a href="#">Mens</a><a href="#">Service</a><a href="#">Products</a><a href="#">Contact</a>
</nav>
<a class="abs btn-outline-header">View Our Prices</a>

<section class="abs hero" role="img" aria-label="Barber trimming a client's beard in a dimly lit salon"></section>
<div class="abs hero-kicker">WELCOME TO <span>MARLOWE DOWN TOWN</span></div>
<h1 class="abs hero-title">WE ARE PROFESSIONAL CARE<br>FOR YOUR HAIR</h1>
<a class="abs btn btn-ghost">Read More</a>
<a class="abs btn btn-gold hero-prices">Our Prices</a>

<div class="abs about-photo" role="img" aria-label="Woman with voluminous auburn curls in profile"></div>
<h2 class="abs section-heading about-heading">About Us</h2>
<div class="abs rule about-rule"></div>
<h3 class="abs about-sub">Experienced and Traditional<br>Stylish Marlowe Downtown Shop</h3>
<div class="abs about-copy">
  <p>At Marlowe Downtown we are committed to providing an unparalleled experience using only the most advanced and innovative techniques to achieve classic and contemporary styles for our clients in the heart of Downtown Grand Rapids.</p>
  <p>Our team is dedicated to the highest level of quality and professionalism, all in a comfortable and relaxing atmosphere.</p>
</div>
<a class="abs btn btn-gold about-btn">Read More</a>

<section class="abs service-band" role="img" aria-label="Close-up of a woman with styled hair on a dark background"></section>
<h2 class="abs section-heading service-heading">Our service</h2>
<div class="abs rule service-rule"></div>

<div class="abs service-card">
  <div class="service" style="left:55px;top:51px"><div class="service-thumb" role="img" aria-label="Women's facial treatment" style="background:linear-gradient(135deg,#f3e4d6,#a9b98f)"></div><h3>Women’s Facial</h3><p>Lorem Ipsum is simply dummy text of the printing and typesetting industry. Lorem Ipsum has been the industry's standard dummy text ever since the 1500s, when an unknown printer took.</p><span class="more">From $55 · Read more →</span></div>
  <div class="service" style="left:303px;top:51px"><div class="service-thumb" role="img" aria-label="Men's facial treatment" style="background:linear-gradient(135deg,#d9b79a,#e9e6e0)"></div><h3>Men’s Facial</h3><p>Lorem Ipsum is simply dummy text of the printing and typesetting industry. Lorem Ipsum has been the industry's standard dummy text ever since the 1500s, when an unknown printer took.</p><span class="more">From $45 · Read more →</span></div>
  <div class="service" style="left:551px;top:51px"><div class="service-thumb" role="img" aria-label="Styled updo haircut" style="background:linear-gradient(135deg,#2a2020,#e8cfc0)"></div><h3>Haircut / Style</h3><p>Lorem Ipsum is simply dummy text of the printing and typesetting industry. Lorem Ipsum has been the industry's standard dummy text ever since the 1500s, when an unknown printer took.</p><span class="more">From $35 · Read more →</span></div>
  <div class="service" style="left:55px;top:330px"><div class="service-thumb" role="img" aria-label="Nail filing" style="background:linear-gradient(135deg,#f6e2da,#e7c0b0)"></div><h3>Women’s Nailcut</h3><p>Lorem Ipsum is simply dummy text of the printing and typesetting industry. Lorem Ipsum has been the industry's standard dummy text ever since the 1500s, when an unknown printer took.</p><span class="more">From $25 · Read more →</span></div>
  <div class="service" style="left:303px;top:330px"><div class="service-thumb" role="img" aria-label="Bridal makeup application" style="background:linear-gradient(135deg,#6b4a3a,#e2b595)"></div><h3>Bridal Services</h3><p>Lorem Ipsum is simply dummy text of the printing and typesetting industry. Lorem Ipsum has been the industry's standard dummy text ever since the 1500s, when an unknown printer took.</p><span class="more">From $120 · Read more →</span></div>
  <div class="service" style="left:551px;top:330px"><div class="service-thumb" role="img" aria-label="Waxing treatment" style="background:linear-gradient(135deg,#dfe8ee,#f0e0cf)"></div><h3>Waxing</h3><p>Lorem Ipsum is simply dummy text of the printing and typesetting industry. Lorem Ipsum has been the industry's standard dummy text ever since the 1500s, when an unknown printer took.</p><span class="more">From $20 · Read more →</span></div>
</div>
<a class="abs btn btn-gold card-btn">See Full Price List</a>

<footer>
  <div class="abs brand footer-brand"><span class="brand-name">MARLOWE</span><span class="brand-sub">DOWNTOWN</span></div>
  <p class="abs footer-about">At Marlowe Downtown we are committed to providing an unparalleled experience using only the most advanced and innovative techniques to achieve classic.</p>

  <div class="abs footer-col links"><h4>Site links</h4><ul><li>Home</li><li>Womens</li><li>Mens</li><li>Service</li><li>Contact</li></ul></div>
  <div class="abs footer-col hours"><h4>Hours of Operation</h4><ul>
    <li>Monday &amp; Wednesday<br>(10 am - 7 pm)</li>
    <li>Tuesday &amp; Thursday<br>(9 am - 7 pm)</li>
    <li>Friday (9 am - 8 pm)</li>
    <li>Saturday (10 am - 3 pm)</li>
    <li>Sunday&nbsp;&nbsp;&nbsp;&nbsp;&nbsp;&nbsp;&nbsp;&nbsp;&nbsp;&nbsp;Closed</li>
  </ul></div>
  <div class="abs footer-col touch">
    <h4>Get in touch</h4>
    <svg style="top:42px" width="16" height="16" viewBox="0 0 16 16"><circle cx="8" cy="8" r="8" fill="var(--gold)"/><path d="M5.2 4.3l1.4-.3.8 1.8-.9.7c.5 1.1 1.2 1.8 2.3 2.3l.7-.9 1.8.8-.3 1.4c-3.2 0-5.8-2.6-5.8-5.8z" fill="#fff"/></svg>
    <span class="touch-line" style="top:42px">616-555-0142</span>
    <span class="touch-line" style="top:65px">616-555-0142</span>
    <svg style="top:99px" width="16" height="16" viewBox="0 0 16 16"><circle cx="8" cy="8" r="8" fill="var(--gold)"/><rect x="4.2" y="5.3" width="7.6" height="5.4" fill="#fff"/><path d="M4.2 5.3L8 8.3l3.8-3" fill="none" stroke="var(--gold)" stroke-width="1"/></svg>
    <span class="touch-line" style="top:99px">hello@marlowedowntown.example</span>
    <svg style="top:139px" width="16" height="16" viewBox="0 0 16 16"><circle cx="8" cy="8" r="8" fill="var(--gold)"/><path d="M8 3.5a3 3 0 0 1 3 3c0 2.2-3 5.8-3 5.8S5 8.7 5 6.5a3 3 0 0 1 3-3z" fill="#fff"/><circle cx="8" cy="6.5" r="1.1" fill="var(--gold)"/></svg>
    <span class="touch-line" style="top:139px">48 Cedar Street N.W. #4</span>
    <span class="touch-line" style="top:160px">Grand Rapids, MI 49500</span>
  </div>

  <div class="abs socials" aria-label="Social links"><span></span><span></span><span></span><span></span><span></span></div>
  <div class="abs copyright-bar">Copyright ©2001-2019, Marlowe Downtown. All rights reserved.</div>
</footer>

</body>
</html>
```